Business Card Design For Marketing Agnecy LWP

Need business card design for marketing agency.

Dorian Pellow
President, CEO
1-555-302-4196
dorian@brightlanepromotions.example
www.BrightlanePromotions.example

Back Side:
Grow Sales With Loyalty Perks, Promotions & Gifts
Request A Free Starter Kit

Target Market(s)

B2B

Industry/Entity Type

Marketing

Contact Information for Business Card

Dorian Pellow
President, CEO
1-555-302-4196

Back Side:
Request A Free Starter Kit

Please note that my current url is OLD DESIGN. I am working on new design and want the business card to match color themes at least on new site. Here is the demo link for new site so you can see the colors I use, etc.

http://pixelquarrydemo.example/dh/dorian/lwp_final/index.html

Requirements
Must have
• Please note that my current url is OLD DESIGN. I am working on new design and want the business card to match color themes at least on new site. Here is the demo link for new site so you can see the colors I use, etc.

Nice to have

Should not have

```html
<!DOCTYPE html>
<html lang="en">
<head>
<meta charset="utf-8">
<title>LWP Business Card</title>
<link rel="stylesheet" href="https://fonts.googleapis.com/css2?family=Montserrat:wght@500;600;700;800&display=swap">
<style>
  :root {
    --brand-blue: #1d74c0;
    --brand-green: #4aa84f;
    --ink-gray: #55595e;
    --ink-dark: #1f1f1f;
    --rule-gray: #5a5d61;
    --paper: #ffffff;
    --backdrop: #eceef0;
    --ghost: #f1f1f1;
  }
  * { box-sizing: border-box; margin: 0; padding: 0; }
  html, body { width: 977px; height: 1200px; overflow: hidden; }
  body {
    background: var(--backdrop);
    font-family: "Montserrat", sans-serif;
    position: relative;
  }
  .card {
    position: absolute;
    left: 68px;
    width: 840px;
    height: 480px;
    background: var(--paper);
    box-shadow: 0 4px 14px rgba(0,0,0,0.14);
    overflow: hidden;
  }
  .card--front { top: 90px; }
  .card--back { top: 630px; }

  /* Front */
  .brand {
    position: absolute;
    left: 0; right: 0;
    top: 78px;
    display: flex;
    justify-content: center;
    align-items: center;
    gap: 14px;
  }
  .brand__dot {
    width: 22px; height: 22px;
    border-radius: 50%;
    background: var(--brand-blue);
  }
  .brand__name {
    font-weight: 800;
    font-size: 112px;
    line-height: 1;
    letter-spacing: -2px;
    color: var(--brand-blue);
  }
  .divider {
    position: absolute;
    top: 305px;
    height: 3px;
    background: var(--rule-gray);
  }
  .divider--left { left: 0; width: 533px; }
  .divider--right { left: 718px; right: 0; }
  .holder {
    position: absolute;
    left: 546px;
    top: 284px;
    width: 162px;
  }
  .holder__name {
    font-weight: 600;
    font-size: 16px;
    line-height: 20px;
    color: var(--brand-blue);
    white-space: nowrap;
  }
  .holder__title {
    font-weight: 600;
    font-size: 14px;
    line-height: 20px;
    color: var(--ink-gray);
    margin-top: 3px;
    white-space: nowrap;
  }
  .contacts {
    position: absolute;
    left: 46px;
    top: 345px;
    list-style: none;
  }
  .contacts__item {
    display: flex;
    align-items: center;
    gap: 11px;
    height: 26px;
    font-weight: 600;
    font-size: 14px;
    color: var(--ink-gray);
    white-space: nowrap;
  }
  .contacts__icon { width: 15px; height: 15px; flex: none; }
  .accent-band {
    position: absolute;
    left: 0; bottom: 0;
    width: 840px; height: 16px;
  }

  /* Back */
  .ghost-name {
    position: absolute;
    left: 0; right: 0;
    top: 70px;
    text-align: center;
    font-weight: 800;
    font-size: 230px;
    line-height: 1;
    color: var(--ghost);
    letter-spacing: -4px;
  }
  .tagline {
    position: absolute;
    left: 0; right: 0;
    top: 222px;
    text-align: center;
    font-weight: 700;
    font-size: 21px;
    color: var(--ink-gray);
    white-space: nowrap;
  }
  .tagline__lead { color: var(--brand-green); }
  .tagline__accent { color: var(--brand-blue); }
  .tagline-rule {
    position: absolute;
    left: 77px;
    width: 686px;
    top: 260px;
    height: 2px;
    background: var(--rule-gray);
  }
  .offer {
    position: absolute;
    left: 0; right: 0;
    top: 269px;
    text-align: center;
    font-weight: 600;
    font-size: 19px;
    color: var(--ink-dark);
    letter-spacing: 0.5px;
  }
  .back-url {
    position: absolute;
    left: 0; right: 0;
    top: 416px;
    text-align: center;
    font-weight: 600;
    font-size: 15px;
    color: var(--ink-dark);
  }
</style>
</head>
<body>

<section class="card card--front" aria-label="Card front">
  <div class="brand">
    <span class="brand__name">LWP</span>
    <span class="brand__dot"></span>
  </div>

  <div class="divider divider--left"></div>
  <div class="holder">
    <p class="holder__name">DORIAN PELLOW</p>
    <p class="holder__title">President, CEO</p>
  </div>
  <div class="divider divider--right"></div>

  <ul class="contacts">
    <li class="contacts__item">
      <svg class="contacts__icon" viewBox="0 0 16 16" aria-hidden="true">
        <path d="M3.5 1.5l2.5 0.5 1 3-1.6 1.2a8 8 0 0 0 4.4 4.4L11 9l3 1 0.5 2.5-1.8 1.8C7 14 2 9 1.7 3.3z" fill="var(--brand-blue)"/>
      </svg>
      1-555-302-4196
    </li>
    <li class="contacts__item">
      <svg class="contacts__icon" viewBox="0 0 16 16" aria-hidden="true">
        <rect x="1" y="3" width="14" height="10" fill="var(--brand-blue)"/>
        <path d="M1 3l7 5.5L15 3" fill="none" stroke="#fff" stroke-width="1.3"/>
      </svg>
      dorian@brightlanepromotions.example
    </li>
    <li class="contacts__item">
      <svg class="contacts__icon" viewBox="0 0 16 16" aria-hidden="true">
        <circle cx="8" cy="8" r="6.5" fill="none" stroke="var(--brand-blue)" stroke-width="1.6"/>
        <path d="M1.5 8h13M8 1.5c-3 3.5-3 9.5 0 13M8 1.5c3 3.5 3 9.5 0 13" fill="none" stroke="var(--brand-blue)" stroke-width="1.1"/>
      </svg>
      www.BrightlanePromotions.example
    </li>
  </ul>

  <svg class="accent-band" viewBox="0 0 840 16" aria-hidden="true">
    <polygon points="0,0 428,0 422,16 0,16" fill="var(--brand-blue)"/>
    <polygon points="432,0 840,0 840,16 426,16" fill="var(--brand-green)"/>
  </svg>
</section>

<section class="card card--back" aria-label="Card back">
  <div class="ghost-name" aria-hidden="true">LWP</div>
  <p class="tagline">
    <span class="tagline__lead">GROW</span> SALES WITH LOYALTY PERKS, PROMOTIONS <span class="tagline__accent">&amp; GIFTS</span>
  </p>
  <div class="tagline-rule"></div>
  <p class="offer">REQUEST A FREE STARTER KIT</p>
  <p class="back-url">www.BrightlanePromotions.example</p>
</section>

</body>
</html>
```